Driving-coach/trainer who wants to inform about the offer and how I can help people to drive more re

I need a flyer that informs potential customers about my offer.

DL size 210 mm x 99 mm, vertical!

I'm a trainer/coach who helps people to drive a car more relaxed, without fear and more confident.

It's a one to one training. I do train people in their own car. It gets people their freedom back to go where and when they like to go by own car...
Updates

Project Deadline Extended Reason: I would like to extend my project... didn't find the time to give feedback because of unexpected other jobs I had to do.Would be great if you could extend my project around 5 more days. THANKS. Added Wednesday, January 4, 2017

Target Market(s)

People (man an woman) who are afraid of driving a car, or are very stressed while driving....

Industry/Entity Type

Life Coaching

Font styles to use
Sans Serif

Colors
acd136

Requirements
Must have
• Page 1:
• -my offer (see text-pdf)
• -three fotos (see attached files "Pixavine") of people who are satisfied with my offer
• Page 2:
• -advantages in the work with me.
• -contact information
• -and a picture of me (see attached file) next to the contact information or the advantages of my work
• -my logo (see attached file) on Page 1 + 2
• -i like a "clear" and structured layout. "Less is more"

```html
<!DOCTYPE html>
<html lang="de">
<head>
<meta charset="utf-8">
<title>Fahrangst-Bewältigungs-Coach – Flyer</title>
<link rel="stylesheet" href="https://fonts.googleapis.com/css2?family=Didact+Gothic&family=Arimo:wght@400;700&family=Lato:wght@400&family=Roboto+Condensed:wght@300;400&display=swap">
<style>
  :root{
    --green:#5aac33;
    --green-light:#6dc23c;
    --green-dark:#469a2c;
    --charcoal:#434343;
    --white:#ffffff;
    --page:#e9e9e9;
  }
  html,body{margin:0;padding:0;width:1200px;height:1200px;overflow:hidden;background:var(--page);}
  .canvas{position:relative;width:1200px;height:1200px;}
  .flyer{
    position:absolute;left:327.5px;top:30px;width:545px;height:1120px;
    transform:scale(1.018);transform-origin:top center;
    background:var(--white);overflow:hidden;
    box-shadow:0 4px 18px rgba(0,0,0,.18);
    font-family:"Arimo",Arial,sans-serif;color:var(--white);
  }
  .flyer-shapes{position:absolute;inset:0;}
  .brand{position:absolute;left:108px;top:33px;color:var(--green);font-family:"Didact Gothic",sans-serif;}
  .brand-name{font-size:30px;letter-spacing:2.5px;line-height:1.1;}
  .brand-role{font-size:21px;letter-spacing:2.3px;margin-top:2px;}
  .hero-photo{
    position:absolute;left:0;top:0;width:545px;height:470px;
    background:linear-gradient(115deg,#8a7a6a 0%,#c59a6a 35%,#d8b18a 55%,#7b7f84 75%,#3c3e42 100%);
    clip-path:polygon(0 160px,360px 232px,545px 186px,545px 425px,280px 458px,0 422px);
  }
  .intro-title{position:absolute;left:44px;top:456px;font-size:23px;font-weight:700;}
  .intro-q{position:absolute;top:496px;font-size:15.5px;line-height:24px;}
  .intro-q.left{left:44px;} .intro-q.right{left:306px;}
  .pill{
    position:absolute;left:113px;width:316px;height:32px;border:2px solid var(--charcoal);
    border-radius:18px;background:var(--white);color:var(--green);
    font-weight:700;font-size:20.5px;text-align:center;line-height:32px;
  }
  .pill.first{top:555px;} .pill.second{top:802px;}
  .benefits{position:absolute;top:604px;list-style:none;margin:0;padding:0;font-family:"Lato",sans-serif;font-size:13.8px;line-height:17.6px;}
  .benefits.left{left:18px;width:255px;} .benefits.right{left:280px;width:250px;}
  .benefits li{position:relative;padding-left:12px;margin-bottom:9px;}
  .benefits li::before{content:"";position:absolute;left:0;top:5px;width:6px;height:6px;border-radius:50%;background:var(--white);}
  .steps-title{position:absolute;left:0;width:545px;top:893px;text-align:center;color:var(--green);font-weight:700;font-size:20px;letter-spacing:.5px;}
  .step{
    position:absolute;width:110px;height:110px;border-radius:50%;background:var(--green);
    border:5px solid var(--white);box-shadow:0 3px 8px rgba(0,0,0,.35);
    display:flex;align-items:center;justify-content:center;text-align:center;
    font-family:"Roboto Condensed",sans-serif;font-weight:300;font-size:16.5px;line-height:22px;
  }
  .step.one{left:30px;top:919px;} .step.two{left:207px;top:914px;} .step.three{left:382px;top:919px;}
  .note{
    position:absolute;left:110px;top:1060px;width:325px;height:50px;box-sizing:border-box;
    background:var(--charcoal);border-radius:9px 9px 0 0;padding:8px 10px;
    font-family:"Roboto Condensed",sans-serif;font-size:11px;line-height:17px;letter-spacing:-.1px;
  }
</style>
</head>
<body>
<div class="canvas">
  <article class="flyer">
    <svg class="flyer-shapes" width="545" height="1120" viewBox="0 0 545 1120" aria-hidden="true">
      <defs>
        <radialGradient id="greenField" cx="50%" cy="45%" r="70%">
          <stop offset="0" stop-color="#6dc23c"/>
          <stop offset="1" stop-color="#469a2c"/>
        </radialGradient>
      </defs>
      <polygon points="0,135 360,207 545,157 545,186 360,232 0,160" fill="var(--green)"/>
      <polygon points="0,432 280,466 545,433 545,897 280,857 0,893" fill="url(#greenField)"/>
      <polygon points="0,893 280,857 545,897 545,920 280,876 0,912" fill="var(--charcoal)"/>
      <rect x="145" y="975" width="70" height="22" fill="var(--green)"/>
      <rect x="325" y="975" width="65" height="22" fill="var(--green)"/>
      <polyline points="455,1043 455,1085 440,1085" fill="none" stroke="var(--green)" stroke-width="2"/>
      <polyline points="446,1079 438,1085 446,1091" fill="none" stroke="var(--green)" stroke-width="2"/>
      <rect x="0" y="1110" width="545" height="10" fill="var(--green)"/>
    </svg>

    <div class="hero-photo" role="img" aria-label="Foto: lächelnde Fahrerin am Steuer eines offenen Cabrios mit hellen Ledersitzen"></div>

    <header class="brand">
      <div class="brand-name">Carla Weinhardt</div>
      <div class="brand-role">Fahrangst-Bewältigungs-Coach</div>
    </header>

    <h2 class="intro-title" style="margin:0">Wollen Sie</h2>
    <p class="intro-q left" style="margin:0">Fahrangst überwinden?<br>Oder einfach sicher Autofahren?</p>
    <p class="intro-q right" style="margin:0">Panikattacken beim<br>Autofahren loswerden?</p>

    <div class="pill first">Dann sind Sie hier richtig!</div>

    <ul class="benefits left">
      <li>Angst oder Panikattacken begleiten Sie beim Autofahren. Vielleicht vermeiden Sie deshalb das Autofahren komplett. - Sie möchten angstfrei und/oder ohne Panikattacken fahren.</li>
      <li>Sie trauen sich das Autofahren nicht (mehr) zu. - Sie wünschen sich, sicher, entspannt und stressfrei Auto zu fahren.</li>
    </ul>
    <ul class="benefits right">
      <li>Autofahren erleben Sie unter hoher Anspannung und Stress. - Sie wünschen sich, Autofahren sicher und entspannt zu erleben.</li>
      <li>Bestimmte Situationen (z.B. Autobahn, Baustellen, Stadtvekehr...) bereiten Ihnen großen Stress. - Sie möchten diese Situationen souveräner meistern.</li>
    </ul>

    <div class="pill second">Das muss nicht so bleiben!</div>

    <h3 class="steps-title" style="margin:0">3 Schritte zur Lösung:</h3>
    <div class="step one">Erstgespräch<br>vereinbaren</div>
    <div class="step two">Analyse Ihrer<br>individuellen<br>Situation und<br>Zielsetzung</div>
    <div class="step three">Individuelles<br>Coaching und<br>Training</div>

    <p class="note" style="margin:0">(ggf. Fahrangst-Therapie - als psychotherapeutische<br>Heilpraktikerin bin ich auf Angst- und Panikstörungen spezialisiert)</p>
  </article>
</div>
</body>
</html>
```